Quorenta - Automated robotic Inspection with AI need new business cards

We need a new design of our business cards. The company is focused on automated quality control at high speed with unmatched results. We have a logo but need a more forward leaning business card that shows that we are delivering cutting edge technology.

Contact Information for Business Card

Name
Position
Adress
Phone
Email
e.g.
Lotta Berglund
Chief Financial Officer (CFO)

Quorenta Sweden AB
Rönnvägen 14, SE-175 43 JÄRFÄLLA, Sweden
Mobile: +46701 23 45 67 | Office: +46 8 52 61 74
www.quorenta-example.com

Font styles to use
Sans Serif

```html
<!DOCTYPE html>
<html lang="en">
<head>
<meta charset="utf-8">
<title>Quorenta – Business Card</title>
<link rel="stylesheet" href="https://fonts.googleapis.com/css2?family=Roboto:wght@400;500;700&display=swap">
<style>
  :root {
    --page: #e9e6e1;
    --card-light: #f4f3f1;
    --brand-blue: #1d6794;
    --brand-blue-deep: #164f73;
    --ink-navy: #1f4f78;
    --text-light: #ffffff;
    --text-soft: #e3edf4;
    --deco-dark: #3a3f44;
  }
  * { margin: 0; padding: 0; box-sizing: border-box; }
  html, body {
    width: 1200px;
    height: 1054px;
    overflow: hidden;
    background: var(--page);
    font-family: "Roboto", Arial, sans-serif;
  }
  .card {
    position: absolute;
    left: 100px;
    top: 227px;
    width: 1000px;
    height: 600px;
    background: var(--brand-blue);
    overflow: hidden;
    box-shadow: 0 10px 30px rgba(0,0,0,0.18);
  }
  .card__header {
    position: absolute;
    left: 0; top: 0;
    width: 100%;
    height: 208px;
    background: var(--card-light);
  }
  .brand {
    position: absolute;
    left: 46px;
    top: 58px;
    display: flex;
    align-items: center;
    gap: 22px;
  }
  .brand__dot {
    width: 58px;
    height: 58px;
    border-radius: 50%;
    background: var(--ink-navy);
  }
  .brand__name {
    font-size: 76px;
    font-weight: 500;
    letter-spacing: 4px;
    color: var(--ink-navy);
    line-height: 1;
  }
  .card__decoration {
    position: absolute;
    right: -40px;
    top: 130px;
    width: 560px;
    height: 440px;
    border-radius: 50%;
    background: radial-gradient(ellipse at 55% 50%, rgba(58,63,68,0.55) 0%, rgba(58,63,68,0.25) 55%, rgba(58,63,68,0) 72%);
  }
  .contact {
    position: absolute;
    left: 60px;
    top: 238px;
    color: var(--text-light);
  }
  .contact__name {
    font-size: 38px;
    font-weight: 700;
    line-height: 1.1;
  }
  .contact__role {
    font-size: 23px;
    font-weight: 400;
    color: var(--text-soft);
    margin-top: 10px;
  }
  .contact__list {
    list-style: none;
    margin-top: 32px;
  }
  .contact__item {
    display: flex;
    align-items: center;
    gap: 20px;
    font-size: 23px;
    line-height: 38px;
  }
  .contact__icon {
    width: 22px;
    height: 22px;
    flex: none;
    fill: var(--text-soft);
  }
  .contact__address {
    font-style: normal;
    font-size: 23px;
    line-height: 37px;
    color: var(--text-soft);
    margin-top: 6px;
  }
</style>
</head>
<body>
  <article class="card">
    <header class="card__header">
      <div class="brand">
        <span class="brand__dot"></span>
        <span class="brand__name">QUORENTA</span>
      </div>
    </header>

    <div class="card__decoration" role="img" aria-label="Large decorative brand symbol area"></div>

    <section class="contact">
      <h1 class="contact__name">Lotta Berglund</h1>
      <p class="contact__role">Chief Financial Officer (CFO)</p>
      <ul class="contact__list">
        <li class="contact__item">
          <svg class="contact__icon" viewBox="0 0 24 24"><path d="M3 7c0-2 2-3 9-3s9 1 9 3v2h-5V7H8v2H3z M6 11h12l2 8H4z M12 13a2.5 2.5 0 1 0 0 5a2.5 2.5 0 1 0 0-5z"/></svg>
          <span>+46 701 23 45 67</span>
        </li>
        <li class="contact__item">
          <svg class="contact__icon" viewBox="0 0 24 24"><path d="M3 7c0-2 2-3 9-3s9 1 9 3v2h-5V7H8v2H3z M6 11h12l2 8H4z M12 13a2.5 2.5 0 1 0 0 5a2.5 2.5 0 1 0 0-5z"/></svg>
          <span>+46 8 52 61 74</span>
        </li>
        <li class="contact__item">
          <svg class="contact__icon" viewBox="0 0 24 24"><path d="M2 5h20v14H2z M4 7v1l8 5l8-5V7l-8 5z" fill-rule="evenodd"/></svg>
          <span>lotta.b@quorenta-example.com</span>
        </li>
        <li class="contact__item">
          <svg class="contact__icon" viewBox="0 0 24 24"><path d="M12 2a10 10 0 1 0 0 20a10 10 0 1 0 0-20z M12 4c1.5 1.8 2.4 4.8 2.5 7h-5C9.6 8.8 10.5 5.8 12 4z M9.5 13h5c-.1 2.2-1 5.2-2.5 7c-1.5-1.8-2.4-4.8-2.5-7z M4.1 11a8 8 0 0 1 4.3-6.2C7.9 6.7 7.6 9 7.5 11z M4.1 13h3.4c.1 2 .4 4.3.9 6.2A8 8 0 0 1 4.1 13z M16.5 11c-.1-2-.4-4.3-.9-6.2A8 8 0 0 1 19.9 11z M16.5 13h3.4a8 8 0 0 1-4.3 6.2c.5-1.9.8-4.2.9-6.2z" fill-rule="evenodd"/></svg>
          <span>www.quorenta-example.com</span>
        </li>
      </ul>
      <address class="contact__address">
        Rönnvägen 14, SE-175<br>
        43 JÄRFÄLLA, Sweden
      </address>
    </section>
  </article>
</body>
</html>
```